Tallowcrest Rise A4 Potrait foldout brochure

We need a brochure design for this residential land development. I have attached the a style that we like to base our design on. Full colour required. will provide files required for design also. PLEASE DO NOT COPY THIS DESIGN. Come up with a new style that gives you this feeling. Please note the plan needs to be positioned landscape on the inside 2 A4 Pages.

Industry/Entity Type

Residential

Other font styles liked:
• Try with Century Gothich

Requirements
Must have
• use same colours as supplied in Tallowcrest rise brochure.
Nice to have
• nice modern simple background graphics

```html
<!DOCTYPE html>
<html lang="en">
<head>
<meta charset="utf-8">
<title>Tallowcrest Rise – Masterplan Brochure Cover</title>
<link href="https://fonts.googleapis.com/css2?family=Questrial&display=swap" rel="stylesheet">
<style>
  :root {
    --forest: #054a20;
    --leaf: #5cb84a;
    --lime: #8cc63f;
    --sun: #f7b21c;
    --amber: #f18f1e;
    --plum: #8e3a96;
    --white: #ffffff;
    --fold: rgba(255, 255, 255, 0.35);
  }
  * { margin: 0; padding: 0; box-sizing: border-box; }
  html, body {
    width: 1200px;
    height: 566px;
    overflow: hidden;
    background: var(--forest);
  }
  .brochure {
    position: relative;
    width: 1200px;
    height: 566px;
    background: var(--forest);
    font-family: "Questrial", "Century Gothic", sans-serif;
    color: var(--white);
    overflow: hidden;
  }
  .pattern-band {
    position: absolute;
    left: 0;
    width: 1200px;
    display: block;
  }
  .pattern-band--top { top: 0; height: 60px; }
  .pattern-band--bottom { bottom: 0; height: 64px; }
  .fold-line {
    position: absolute;
    top: 0;
    bottom: 0;
    width: 0;
    border-left: 1px dashed var(--fold);
  }
  .fold-line--first { left: 400px; }
  .fold-line--second { left: 800px; }
  .panel {
    position: absolute;
    top: 0;
    width: 400px;
    height: 566px;
    text-align: center;
  }
  .panel--inner-flap { left: 0; }
  .panel--back { left: 400px; }
  .panel--front { left: 800px; }
  .brand-name {
    position: absolute;
    left: 0;
    right: 0;
    line-height: 1;
    font-weight: 400;
    color: var(--white);
    white-space: nowrap;
  }
  .brand-locale {
    position: absolute;
    font-size: 5px;
    line-height: 1;
    color: var(--leaf);
    white-space: nowrap;
  }
  .panel--inner-flap .brand-name { top: 226px; font-size: 15.5px; }
  .panel--inner-flap .brand-locale { top: 241px; left: 240px; }
  .intro {
    position: absolute;
    top: 263px;
    left: 84px;
    width: 232px;
    font-size: 10.6px;
    line-height: 16px;
    color: var(--white);
  }
  .panel--back .brand-name { top: 278px; font-size: 13.5px; }
  .panel--front .brand-name { top: 287px; font-size: 30px; }
  .panel--front .brand-locale { top: 318px; left: 274px; font-size: 7px; }
  .document-title {
    position: absolute;
    top: 368px;
    left: 0;
    right: 0;
    font-size: 33px;
    font-weight: 400;
    line-height: 1;
    color: var(--leaf);
  }
</style>
</head>
<body>
<main class="brochure">
  <svg class="pattern-band pattern-band--top" viewBox="0 0 1200 60" preserveAspectRatio="none" role="img" aria-label="Faceted border of green, yellow and purple triangles">
    <defs>
      <linearGradient id="band-top" x1="0" y1="0" x2="1" y2="0">
        <stop offset="0" stop-color="#5cb84a"/>
        <stop offset="0.2" stop-color="#f7b21c"/>
        <stop offset="0.4" stop-color="#8cc63f"/>
        <stop offset="0.6" stop-color="#8e3a96"/>
        <stop offset="0.8" stop-color="#f7b21c"/>
        <stop offset="1" stop-color="#5cb84a"/>
      </linearGradient>
    </defs>
    <path d="M0 0H1200V44L1140 38L1080 50L1000 30L930 48L860 36L800 58L740 40L660 46L560 26L470 50L400 36L330 44L250 22L170 40L90 30L30 52L0 44Z" fill="url(#band-top)"/>
  </svg>

  <svg class="pattern-band pattern-band--bottom" viewBox="0 0 1200 64" preserveAspectRatio="none" role="img" aria-label="Faceted border of green, yellow and purple triangles">
    <defs>
      <linearGradient id="band-bottom" x1="0" y1="0" x2="1" y2="0">
        <stop offset="0" stop-color="#8e3a96"/>
        <stop offset="0.2" stop-color="#5cb84a"/>
        <stop offset="0.45" stop-color="#f7b21c"/>
        <stop offset="0.65" stop-color="#8cc63f"/>
        <stop offset="0.85" stop-color="#8e3a96"/>
        <stop offset="1" stop-color="#f18f1e"/>
      </linearGradient>
    </defs>
    <path d="M0 64H1200V12L1130 20L1060 6L990 22L910 10L840 24L800 2L760 18L690 8L610 24L540 12L470 20L400 4L340 18L260 8L190 22L110 12L40 20L0 10Z" fill="url(#band-bottom)"/>
  </svg>

  <span class="fold-line fold-line--first"></span>
  <span class="fold-line fold-line--second"></span>

  <section class="panel panel--inner-flap">
    <h2 class="brand-name">Tallowcrest Rise</h2>
    <span class="brand-locale">Ashvale Park</span>
    <p class="intro">Tallowcrest Rise is a boutique residential land release that consists of 47 generously sized blocks that have been designed for families looking for larger style blocks, positioned conveniently close to Kestrel Vale and minutes away from Marrowick.</p>
  </section>

  <section class="panel panel--back">
    <h2 class="brand-name">Tallowcrest Rise</h2>
  </section>

  <section class="panel panel--front">
    <h1 class="brand-name">Tallowcrest Rise</h1>
    <span class="brand-locale">Ashvale Park</span>
    <p class="document-title">Masterplan</p>
  </section>
</main>
</body>
</html>
```